Company letter head

Hello,
We are a global logistics company requiring a letterhead design for all our company documentation.
Company Name: Clearly display the full name of your company at the top of the letterhead.
Logo: Include your company logo for brand recognition.
Contact Information: This includes your company's address, phone number, email address, and website URL.
Target Market(s)
Clients/customers
Industry/Entity Type
Logistics
Font styles to use
Sans Serif
Requirements
Must have
- Company name and logo
Nice to have
- borders, header/footers

```html
<!DOCTYPE html>
<html lang="en">
<head>
<meta charset="utf-8">
<title>Northwind Freight Lines — Letterhead</title>
<link href="https://fonts.googleapis.com/css2?family=Open+Sans:wght@400;700&display=swap" rel="stylesheet">
<style>
  :root {
    --brand-red: #e0252b;
    --ink: #2b2b2b;
    --paper: #ffffff;
    --backdrop: #c4c4c4;
  }
  * { box-sizing: border-box; margin: 0; padding: 0; }
  html, body {
    width: 1200px;
    height: 686px;
    overflow: hidden;
    background: var(--backdrop);
    font-family: "Open Sans", Arial, sans-serif;
  }
  .canvas {
    width: 1200px;
    height: 686px;
    display: flex;
    align-items: center;
    justify-content: center;
  }
  .letterhead {
    position: relative;
    width: 458px;
    height: 648px;
    background: var(--paper);
  }
  .brand {
    position: absolute;
    top: 38px;
    left: 38px;
    display: flex;
    align-items: center;
    gap: 8px;
  }
  .brand-mark {
    width: 14px;
    height: 14px;
    border-radius: 50%;
    background: var(--brand-red);
  }
  .brand-name {
    font-weight: 700;
    font-size: 15px;
    color: var(--brand-red);
    letter-spacing: 0.2px;
    text-transform: uppercase;
  }
  .contact {
    position: absolute;
    right: 34px;
    bottom: 36px;
    list-style: none;
    font-size: 9.5px;
    line-height: 1.35;
    color: var(--ink);
    text-align: right;
  }
  .contact-item {
    display: flex;
    justify-content: flex-end;
    align-items: flex-start;
    gap: 7px;
    margin-top: 5px;
  }
  .contact-item svg {
    width: 10px;
    height: 10px;
    flex: none;
    margin-top: 2px;
    fill: var(--brand-red);
  }
</style>
</head>
<body>
<main class="canvas">
  <article class="letterhead">
    <header class="brand">
      <span class="brand-mark"></span>
      <span class="brand-name">Northwind Freight Lines</span>
    </header>

    <ul class="contact">
      <li class="contact-item">
        <span>27 Harbour Row<br>Maidstone, Kent, ME14 2QT</span>
        <svg viewBox="0 0 10 10" aria-hidden="true"><path d="M5 0a3.6 3.6 0 0 0-3.6 3.6C1.4 6.3 5 10 5 10s3.6-3.7 3.6-6.4A3.6 3.6 0 0 0 5 0zm0 5a1.4 1.4 0 1 1 0-2.8A1.4 1.4 0 0 1 5 5z"/></svg>
      </li>
      <li class="contact-item">
        <span>(555) 014-2290</span>
        <svg viewBox="0 0 10 10" aria-hidden="true"><path d="M2.2 0.5l1.6 2-1 1.1a6 6 0 0 0 3.6 3.6l1.1-1 2 1.6-1 1.7C4.6 9.5 0.5 5.4 0.5 1.5z"/></svg>
      </li>
      <li class="contact-item">
        <span>www.northwindfreight.com</span>
        <svg viewBox="0 0 10 10" aria-hidden="true"><path d="M5 0a5 5 0 1 0 0 10A5 5 0 0 0 5 0zm0 1c.6 0 1.3 1.4 1.4 3.5H3.6C3.7 2.4 4.4 1 5 1zM3.6 5.5h2.8C6.3 7.6 5.6 9 5 9s-1.3-1.4-1.4-3.5zM1 5.5h1.6c0 1.3.3 2.4.7 3.1A4 4 0 0 1 1 5.5zm0-1a4 4 0 0 1 2.3-3.1c-.4.7-.7 1.8-.7 3.1zm6.4 1H9a4 4 0 0 1-2.3 3.1c.4-.7.7-1.8.7-3.1zm0-1c0-1.3-.3-2.4-.7-3.1A4 4 0 0 1 9 4.5z"/></svg>
      </li>
      <li class="contact-item">
        <span>info@northwindfreight.com</span>
        <svg viewBox="0 0 10 10" aria-hidden="true"><path d="M0 2h10v6H0zm1 .8V3l4 2.6L9 3v-.2zm0 1.3V7h8V4.1L5 6.7z"/></svg>
      </li>
    </ul>
  </article>
</main>
</body>
</html>
```